Financial Services Company power point theme design

We need a PowerPoint theme designed for client presentations and company orientations. We do like modern designs using blue colors. attached is our logos the logo colors may change as needed to fit the theme. Landscape 16: 9 is acceptable

Industry/Entity Type

Financial Service

Colors

Designer to choose colors to be used in the design.

```html
<!DOCTYPE html>
<html lang="en">
<head>
<meta charset="utf-8">
<title>Northbay Financial Group – Presentation Theme</title>
<link href="https://fonts.googleapis.com/css2?family=Montserrat:wght@300;400;600;700&display=swap" rel="stylesheet">
<style>
:root{
  --canvas:#a3a3a3;
  --navy:#1f3a6e;
  --navy-deep:#172d57;
  --ink:#3a3a3a;
  --muted:#8c8c8c;
  --rule:#d6d9df;
  --soft:#eef0f4;
  --grey-block:#9a9a9a;
  --charcoal:#3b3b3b;
  --photo-a:#b9bcc2;
  --photo-b:#6f747c;
  --white:#ffffff;
}
*{box-sizing:border-box;margin:0;padding:0}
html,body{width:938px;height:1200px;overflow:hidden;background:var(--canvas)}
body{font-family:"Montserrat",sans-serif;color:var(--ink)}
.sheet{display:grid;grid-template-columns:repeat(4,221.6px);grid-auto-rows:124px;gap:6.4px;padding:14.4px 17.6px}
.slide{position:relative;background:var(--white);overflow:hidden}
.abs{position:absolute}
.title{position:absolute;left:11px;top:9px;font-size:4.4px;letter-spacing:.2px;color:var(--muted);font-weight:300;text-transform:uppercase}
.title b{color:var(--navy);font-weight:600}
.foot-brand{position:absolute;left:11px;bottom:4px;display:flex;align-items:center;gap:2px;font-size:2.4px;font-weight:600;color:var(--navy);line-height:2.6px;text-transform:uppercase}
.mark{display:inline-block;width:5px;height:5px;background:var(--navy)}
.foot-chev{position:absolute;right:7px;bottom:3px;width:14px;height:7px}
.foot-note{position:absolute;right:24px;bottom:5px;font-size:2px;color:#b4b4b4}
.p{font-size:2.4px;line-height:3.4px;color:var(--muted)}
.h{font-size:2.7px;font-weight:700;color:var(--navy);text-transform:uppercase;margin-bottom:1px}
.hw{font-size:2.7px;font-weight:700;color:var(--white);text-transform:uppercase;margin-bottom:1px}
.pw{font-size:2.4px;line-height:3.4px;color:#c9d3e6}
.photo{position:absolute;background:linear-gradient(135deg,var(--photo-a),var(--photo-b))}
.photo.dark{background:linear-gradient(135deg,#5b616b,#23272e)}
.photo.light{background:linear-gradient(135deg,#e4e6ea,#b5b9c0)}
.photo.warm{background:linear-gradient(135deg,#c8c2bb,#6b625c)}
.navy{background:var(--navy)}
.sq{position:absolute;width:8px;height:8px;background:var(--navy);color:#fff;font-size:2.6px;font-weight:700;display:flex;align-items:center;justify-content:center}
.brand-big{font-weight:600;color:var(--navy);text-transform:uppercase;display:flex;align-items:center;gap:3px}
ul.b{list-style:none}
ul.b li{position:relative;padding-left:3px}
ul.b li:before{content:"";position:absolute;left:0;top:1.3px;width:1.2px;height:1.2px;background:var(--navy);border-radius:50%}
.icon-box{position:absolute;width:10px;height:10px;background:var(--navy)}
.icon-box svg{width:100%;height:100%}
</style>
</head>
<body>
<svg width="0" height="0" style="position:absolute">
  <defs>
    <symbol id="chev" viewBox="0 0 14 7"><path d="M1 1l3 2.5L1 6M5 1l3 2.5L5 6" fill="none" stroke="#9aa6bf" stroke-width="1"/><path d="M8 0l5 3.5L8 7z" fill="#1f3a6e"/></symbol>
    <symbol id="target" viewBox="0 0 10 10"><circle cx="5" cy="5" r="3" fill="none" stroke="#fff" stroke-width=".7"/><circle cx="5" cy="5" r="1.3" fill="none" stroke="#fff" stroke-width=".7"/><path d="M5 5l3.2-3.2" stroke="#fff" stroke-width=".7"/></symbol>
    <symbol id="chart" viewBox="0 0 10 10"><path d="M2.5 7.5V5M4.5 7.5V3.5M6.5 7.5V4.5M2 8h6" stroke="#fff" stroke-width=".8" fill="none"/></symbol>
    <symbol id="case" viewBox="0 0 10 10"><rect x="2.3" y="3.7" width="5.4" height="3.8" fill="none" stroke="#fff" stroke-width=".7"/><path d="M4 3.7V2.8h2v.9" fill="none" stroke="#fff" stroke-width=".7"/></symbol>
    <symbol id="doc" viewBox="0 0 10 10"><rect x="3" y="2" width="4" height="6" fill="none" stroke="#fff" stroke-width=".7"/><path d="M4 4h2M4 5.5h2" stroke="#fff" stroke-width=".6"/></symbol>
  </defs>
</svg>

<main class="sheet">

<!-- 1 Title -->
<section class="slide">
  <div class="brand-big abs" style="left:0;right:0;top:17px;justify-content:center;font-size:4.2px"><span class="mark" style="width:7px;height:7px"></span>Northbay Financial Group</div>
  <div class="abs navy" style="left:0;right:0;top:36px;height:81px">
    <div class="abs" style="left:76px;top:38px;font-size:6px;color:#fff;font-weight:400">PRESENTATION TITLE</div>
    <div class="abs" style="left:76px;top:46px;font-size:2.8px;color:#9fb0d0">PRESENTATION SUBTITLE GOES HERE</div>
    <div class="abs" style="left:88px;bottom:4px;font-size:2px;color:#9fb0d0">Presented by Alex Reed &nbsp;|&nbsp; July 12, 2024</div>
  </div>
</section>

<!-- 2 Title alt -->
<section class="slide">
  <svg class="abs" style="left:0;top:0" width="221.6" height="124" viewBox="0 0 221.6 124"><polygon points="85,0 221.6,0 221.6,124 85,124 78,62" fill="#1f3a6e"/><polygon points="85,0 118,0 118,124 85,124 78,62" fill="#172d57"/></svg>
  <div class="brand-big abs" style="left:14px;top:58px;font-size:3px;flex-direction:column;gap:2px;text-align:center"><span class="mark" style="width:8px;height:8px"></span>Northbay<br>Financial Group</div>
  <div class="abs" style="left:96px;top:54px;font-size:5.6px;color:#fff">PRESENTATION TITLE</div>
  <div class="abs" style="left:96px;top:62px;font-size:2.6px;color:#9fb0d0">PRESENTATION SUBTITLE GOES HERE</div>
  <div class="abs" style="left:96px;bottom:5px;font-size:2px;color:#9fb0d0">Presented by Alex Reed &nbsp;|&nbsp; July 12, 2024</div>
</section>

<!-- 3 TOC -->
<section class="slide">
  <div class="abs" style="left:18px;top:56px;font-size:4.4px;color:var(--muted)"><b style="color:var(--navy);font-weight:600">TABLE</b> OF CONTENT</div>
  <div class="abs p" style="left:18px;top:63px;width:58px">A quick look at the topics covered in this deck.</div>
  <div class="abs" style="left:82px;top:34px;width:.5px;height:60px;background:var(--rule)"></div>
  <div class="abs" style="left:90px;top:35px;width:50px;display:grid;row-gap:6px">
    <div><div class="h">01. Heading text</div><div class="p">Short note on this topic.</div></div>
    <div><div class="h">02. Heading text</div><div class="p">Short note on this topic.</div></div>
    <div><div class="h">03. Heading text</div><div class="p">Short note on this topic.</div></div>
    <div><div class="h">04. Heading text</div><div class="p">Short note on this topic.</div></div>
  </div>
  <div class="abs" style="left:150px;top:35px;width:50px;display:grid;row-gap:6px">
    <div><div class="h">05. Heading text</div><div class="p">Short note on this topic.</div></div>
    <div><div class="h">06. Heading text</div><div class="p">Short note on this topic.</div></div>
    <div><div class="h">07. Heading text</div><div class="p">Short note on this topic.</div></div>
    <div><div class="h">08. Heading text</div><div class="p">Short note on this topic.</div></div>
  </div>
</section>

<!-- 4 TOC grid -->
<section class="slide">
  <div class="title"><b>Table</b> of content</div>
  <div class="sq" style="left:23px;top:40px">01</div><div class="abs" style="left:34px;top:40px;width:40px"><div class="h">Heading text</div><div class="p">Brief line about it.</div></div>
  <div class="sq" style="left:23px;top:62px">02</div><div class="abs" style="left:34px;top:62px;width:40px"><div class="h">Heading text</div><div class="p">Brief line about it.</div></div>
  <div class="sq" style="left:23px;top:84px">03</div><div class="abs" style="left:34px;top:84px;width:40px"><div class="h">Heading text</div><div class="p">Brief line about it.</div></div>
  <div class="sq" style="left:87px;top:40px">04</div><div class="abs" style="left:98px;top:40px;width:40px"><div class="h">Heading text</div><div class="p">Brief line about it.</div></div>
  <div class="sq" style="left:87px;top:62px">05</div><div class="abs" style="left:98px;top:62px;width:40px"><div class="h">Heading text</div><div class="p">Brief line about it.</div></div>
  <div class="sq" style="left:87px;top:84px">06</div><div class="abs" style="left:98px;top:84px;width:40px"><div class="h">Heading text</div><div class="p">Brief line about it.</div></div>
  <div class="sq" style="left:148px;top:40px">07</div><div class="abs" style="left:159px;top:40px;width:40px"><div class="h">Heading text</div><div class="p">Brief line about it.</div></div>
  <div class="sq" style="left:148px;top:62px">08</div><div class="abs" style="left:159px;top:62px;width:40px"><div class="h">Heading text</div><div class="p">Brief line about it.</div></div>
  <div class="sq" style="left:148px;top:84px">09</div><div class="abs" style="left:159px;top:84px;width:40px"><div class="h">Heading text</div><div class="p">Brief line about it.</div></div>
</section>

<!-- 5 Our company -->
<section class="slide">
  <div class="photo" role="img" aria-label="Bright open-plan office lounge" style="left:0;top:0;width:100%;height:74px"></div>
  <div class="abs navy" style="left:0;top:28px;width:100px;height:46px;opacity:.95">
    <div class="abs" style="left:11px;top:12px;font-size:4.4px;color:#fff">OUR COMPANY</div>
    <div class="abs pw" style="left:11px;top:20px;width:76px;font-style:italic">"We help clients plan, grow and protect their wealth with care."</div>
  </div>
  <div class="icon-box" style="left:18px;top:87px"><svg><use href="#chart"/></svg></div><div class="abs" style="left:31px;top:87px;width:40px"><div class="h">Heading text</div><div class="p">Brief line about it.</div></div>
  <div class="icon-box" style="left:86px;top:87px"><svg><use href="#case"/></svg></div><div class="abs" style="left:99px;top:87px;width:40px"><div class="h">Heading text</div><div class="p">Brief line about it.</div></div>
  <div class="icon-box" style="left:154px;top:87px"><svg><use href="#target"/></svg></div><div class="abs" style="left:167px;top:87px;width:40px"><div class="h">Heading text</div><div class="p">Brief line about it.</div></div>
</section>

<!-- 6 Photo with box -->
<section class="slide">
  <div class="photo light" role="img" aria-label="Conference room with white table and black chairs" style="inset:0"></div>
  <div class="abs navy" style="left:0;top:64px;width:92px;height:60px">
    <div class="hw abs" style="left:11px;top:8px">Heading text</div>
    <div class="abs pw" style="left:11px;top:13px;width:72px">Our team brings clear advice and steady support to every client we serve.</div>
  </div>
</section>

<!-- 7 Our company alt -->
<section class="slide">
  <div class="photo light" role="img" aria-label="Conference room with white table and black chairs" style="inset:0"></div>
  <div class="abs navy" style="left:0;top:0;width:92px;height:124px">
    <div class="abs" style="left:0;right:0;top:20px;display:flex;flex-direction:column;align-items:center;gap:2px;font-size:2.8px;font-weight:600;color:#fff;text-align:center;text-transform:uppercase"><span class="mark" style="width:8px;height:8px;background:#fff"></span>Northbay<br>Financial Group</div>
    <div class="abs" style="left:11px;top:56px;font-size:4.4px;color:#fff">OUR COMPANY</div>
    <div class="abs pw" style="left:11px;top:64px;width:72px">Founded on trust, we guide families and firms through every stage of financial life with plain answers.</div>
  </div>
</section>

<!-- 8 One column -->
<section class="slide">
  <div class="title"><b>One column</b> text slide</div>
  <div class="abs p" style="left:11px;top:20px;width:199px;display:grid;row-gap:3px">
    <div>This slide holds a single column of body copy. Use it to explain an idea in full sentences, keeping each paragraph short and focused so the audience can follow along with ease.</div>
    <div>Add a second paragraph to expand the point with detail, figures or a short example drawn from client work.</div>
    <div>A third paragraph can close the thought and lead into the next slide in the deck.</div>
    <div>Keep the tone calm, clear and direct throughout the whole presentation.</div>
  </div>
  <div class="foot-brand"><span class="mark"></span>Northbay<br>Financial</div><div class="foot-note">northbayfinancial.com</div><svg class="foot-chev"><use href="#chev"/></svg>
</section>

<!-- 9 Two column -->
<section class="slide">
  <div class="title"><b>Two column</b> text slide</div>
  <div class="abs" style="left:11px;top:22px;width:95px"><div class="h" style="color:var(--ink)">Opening point here</div><div class="p">Body copy sits in two even columns. Each one carries a short, clear message.</div>
    <ul class="b p" style="margin-top:3px"><li>First supporting point here.</li><li>Second supporting point here.</li><li>Third supporting point here.</li></ul></div>
  <div class="abs" style="left:115px;top:22px;width:95px"><div class="h" style="color:var(--ink)">Second point here</div><div class="p">Use this side to contrast or extend the idea set out on the left.</div>
    <ul class="b p" style="margin-top:3px"><li>First supporting point here.</li><li>Second supporting point here.</li><li>Third supporting point here.</li></ul></div>
  <div class="foot-brand"><span class="mark"></span>Northbay<br>Financial</div><div class="foot-note">northbayfinancial.com</div><svg class="foot-chev"><use href="#chev"/></svg>
</section>

<!-- 10 Bullet -->
<section class="slide">
  <div class="title"><b>Bullet</b> text slide</div>
  <div class="abs" style="left:14px;top:22px;width:92px;display:grid;row-gap:5px">
    <div><div class="h">• Heading text</div><div class="p">A short line that explains this first point.</div></div>
    <div><div class="h">• Heading text</div><div class="p">A short line that explains this next point.</div></div>
    <div><div class="h">• Heading text</div><div class="p">A short line that explains this last point.</div></div>
  </div>
  <div class="abs" style="left:116px;top:22px;width:92px;display:grid;row-gap:5px">
    <div><div class="h">• Heading text</div><div class="p">A short line that explains this first point.</div></div>
    <div><div class="h">• Heading text</div><div class="p">A short line that explains this next point.</div></div>
    <div><div class="h">• Heading text</div><div class="p">A short line that explains this last point.</div></div>
  </div>
  <div class="foot-brand"><span class="mark"></span>Northbay<br>Financial</div><div class="foot-note">northbayfinancial.com</div><svg class="foot-chev"><use href="#chev"/></svg>
</section>

<!-- 11 Section divider -->
<section class="slide navy">
  <svg class="abs" style="left:27px;top:52px" width="17" height="17"><use href="#target"/></svg>
  <div class="abs" style="left:27px;top:83px;font-size:4.4px;color:#fff">SECTION DIVIDER</div>
  <div class="abs pw" style="left:27px;top:90px;width:110px">A short line that introduces the section ahead.</div>
</section>

<!-- 12 What we do -->
<section class="slide">
  <div class="title"><b>What we do</b></div>
  <div class="photo" role="img" aria-label="Office lounge with people at work" style="left:0;top:20px;width:100%;height:50px"></div>
  <div class="icon-box" style="left:33px;top:64px"><svg><use href="#chart"/></svg></div>
  <div class="icon-box" style="left:81px;top:64px"><svg><use href="#doc"/></svg></div>
  <div class="icon-box" style="left:130px;top:64px"><svg><use href="#case"/></svg></div>
  <div class="icon-box" style="left:178px;top:64px"><svg><use href="#target"/></svg></div>
  <div class="abs" style="left:20px;top:78px;width:36px;text-align:center"><div class="h">Heading text</div><div class="p">Brief line about it.</div></div>
  <div class="abs" style="left:68px;top:78px;width:36px;text-align:center"><div class="h">Heading text</div><div class="p">Brief line about it.</div></div>
  <div class="abs" style="left:117px;top:78px;width:36px;text-align:center"><div class="h">Heading text</div><div class="p">Brief line about it.</div></div>
  <div class="abs" style="left:165px;top:78px;width:36px;text-align:center"><div class="h">Heading text</div><div class="p">Brief line about it.</div></div>
  <div class="foot-brand"><span class="mark"></span>Northbay<br>Financial</div><svg class="foot-chev"><use href="#chev"/></svg>
</section>

<!-- 13 Our service -->
<section class="slide">
  <div class="title"><b>Our service</b></div>
  <div class="abs" style="left:79px;top:33px;width:29px;height:29px;background:var(--grey-block)"><svg width="29" height="29" viewBox="-4 -4 18 18"><use href="#target"/></svg></div>
  <div class="abs navy" style="left:111px;top:33px;width:29px;height:29px"><svg width="29" height="29" viewBox="-4 -4 18 18"><use href="#case"/></svg></div>
  <div class="abs navy" style="left:79px;top:65px;width:29px;height:29px"><svg width="29" height="29" viewBox="-4 -4 18 18"><use href="#target"/></svg></div>
  <div class="abs" style="left:111px;top:65px;width:29px;height:29px;background:var(--grey-block)"><svg width="29" height="29" viewBox="-4 -4 18 18"><use href="#chart"/></svg></div>
  <div class="abs" style="left:32px;top:40px;width:42px;text-align:right"><div class="h">Heading text</div><div class="p">A brief line about this service.</div></div>
  <div class="abs" style="left:32px;top:72px;width:42px;text-align:right"><div class="h">Heading text</div><div class="p">A brief line about this service.</div></div>
  <div class="abs" style="left:146px;top:40px;width:42px"><div class="h">Heading text</div><div class="p">A brief line about this service.</div></div>
  <div class="abs" style="left:146px;top:72px;width:42px"><div class="h">Heading text</div><div class="p">A brief line about this service.</div></div>
  <div class="foot-brand"><span class="mark"></span>Northbay<br>Financial</div><svg class="foot-chev"><use href="#chev"/></svg>
</section>

<!-- 14 Our service alt -->
<section class="slide">
  <div class="title"><b>Our service</b></div>
  <div class="abs" style="left:111px;top:0;width:111px;height:124px;background:linear-gradient(135deg,#2a4679,#172d57)" role="img" aria-label="City buildings in navy tone"></div>
  <div class="abs" style="left:19px;top:33px;width:9px;height:9px;border-radius:50%;background:var(--navy)"><svg width="9" height="9"><use href="#target"/></svg></div>
  <div class="abs" style="left:19px;top:58px;width:9px;height:9px;border-radius:50%;background:var(--grey-block)"><svg width="9" height="9"><use href="#target"/></svg></div>
  <div class="abs" style="left:19px;top:83px;width:9px;height:9px;border-radius:50%;background:var(--navy)"><svg width="9" height="9"><use href="#case"/></svg></div>
  <div class="abs" style="left:31px;top:33px;width:60px"><div class="h">Heading text</div><div class="p">A brief line about this service.</div></div>
  <div class="abs" style="left:31px;top:58px;width:60px"><div class="h">Heading text</div><div class="p">A brief line about this service.</div></div>
  <div class="abs" style="left:31px;top:83px;width:60px"><div class="h">Heading text</div><div class="p">A brief line about this service.</div></div>
  <div class="abs" style="left:103px;top:33px;width:9px;height:9px;border-radius:50%;background:var(--navy);border:.6px solid #fff"><svg width="8" height="8"><use href="#chart"/></svg></div>
  <div class="abs" style="left:103px;top:58px;width:9px;height:9px;border-radius:50%;background:var(--grey-block);border:.6px solid #fff"><svg width="8" height="8"><use href="#target"/></svg></div>
  <div class="abs" style="left:103px;top:83px;width:9px;height:9px;border-radius:50%;background:var(--grey-block);border:.6px solid #fff"><svg width="8" height="8"><use href="#doc"/></svg></div>
  <div class="abs" style="left:116px;top:33px;width:60px"><div class="hw">Heading text</div><div class="pw">A brief line about this service.</div></div>
  <div class="abs" style="left:116px;top:58px;width:60px"><div class="hw">Heading text</div><div class="pw">A brief line about this service.</div></div>
  <div class="abs" style="left:116px;top:83px;width:60px"><div class="hw">Heading text</div><div class="pw">A brief line about this service.</div></div>
  <div class="foot-brand"><span class="mark"></span>Northbay<br>Financial</div><svg class="foot-chev"><use href="#chev"/></svg>
</section>

<!-- 15 Team 8 -->
<section class="slide">
  <div class="title"><b>Our team</b></div>
  <div class="photo warm" role="img" aria-label="Team member portrait" style="left:28px;top:28px;width:29px;height:29px"></div>
  <div class="photo warm" role="img" aria-label="Team member portrait" style="left:73px;top:28px;width:29px;height:29px"></div>
  <div class="photo warm" role="img" aria-label="Team member portrait" style="left:118px;top:28px;width:29px;height:29px"></div>
  <div class="photo warm" role="img" aria-label="Team member portrait" style="left:163px;top:28px;width:29px;height:29px"></div>
  <div class="photo warm" role="img" aria-label="Team member portrait" style="left:28px;top:68px;width:29px;height:29px"></div>
  <div class="photo warm" role="img" aria-label="Team member portrait" style="left:73px;top:68px;width:29px;height:29px"></div>
  <div class="photo warm" role="img" aria-label="Team member portrait" style="left:118px;top:68px;width:29px;height:29px"></div>
  <div class="photo warm" role="img" aria-label="Team member portrait" style="left:163px;top:68px;width:29px;height:29px"></div>
  <div class="abs navy" style="left:28px;top:57px;width:29px;height:4px;font-size:2px;color:#fff;text-align:center;line-height:4px">Name Here</div>
  <div class="abs navy" style="left:73px;top:57px;width:29px;height:4px;font-size:2px;color:#fff;text-align:center;line-height:4px">Name Here</div>
  <div class="abs navy" style="left:118px;top:57px;width:29px;height:4px;font-size:2px;color:#fff;text-align:center;line-height:4px">Name Here</div>
  <div class="abs navy" style="left:163px;top:57px;width:29px;height:4px;font-size:2px;color:#fff;text-align:center;line-height:4px">Name Here</div>
  <div class="abs navy" style="left:28px;top:97px;width:29px;height:4px;font-size:2px;color:#fff;text-align:center;line-height:4px">Name Here</div>
  <div class="abs navy" style="left:73px;top:97px;width:29px;height:4px;font-size:2px;color:#fff;text-align:center;line-height:4px">Name Here</div>
  <div class="abs navy" style="left:118px;top:97px;width:29px;height:4px;font-size:2px;color:#fff;text-align:center;line-height:4px">Name Here</div>
  <div class="abs navy" style="left:163px;top:97px;width:29px;height:4px;font-size:2px;color:#fff;text-align:center;line-height:4px">Name Here</div>
  <div class="foot-brand"><span class="mark"></span>Northbay<br>Financial</div><svg class="foot-chev"><use href="#chev"/></svg>
</section>

<!-- 16 Team 3 -->
<section class="slide">
  <div class="title"><b>Our team</b></div>
  <div class="photo warm" role="img" aria-label="Team member portrait" style="left:40px;top:31px;width:30px;height:30px"></div>
  <div class="photo warm" role="img" aria-label="Team member portrait" style="left:96px;top:31px;width:30px;height:30px"></div>
  <div class="photo warm" role="img" aria-label="Team member portrait" style="left:153px;top:31px;width:30px;height:30px"></div>
  <div class="abs" style="left:25px;top:64px;width:60px;text-align:center"><div class="h">Name here</div><div class="p" style="font-size:2px">Manager</div><div class="p" style="margin-top:2px">A short profile of this team member and their role.</div></div>
  <div class="abs" style="left:81px;top:64px;width:60px;text-align:center"><div class="h">Name here</div><div class="p" style="font-size:2px">Manager</div><div class="p" style="margin-top:2px">A short profile of this team member and their role.</div></div>
  <div class="abs" style="left:138px;top:64px;width:60px;text-align:center"><div class="h">Name here</div><div class="p" style="font-size:2px">Manager</div><div class="p" style="margin-top:2px">A short profile of this team member and their role.</div></div>
  <div class="foot-brand"><span class="mark"></span>Northbay<br>Financial</div><svg class="foot-chev"><use href="#chev"/></svg>
</section>

<!-- 17 History -->
<section class="slide">
  <div class="title"><b>Our history</b></div>
  <svg class="abs" style="left:0;top:0" width="221.6" height="124">
    <line x1="15" y1="63" x2="210" y2="63" stroke="#c9ccd2" stroke-width=".5"/>
    <g fill="#1f3a6e"><circle cx="35" cy="63" r="1.3"/><circle cx="73" cy="63" r="1.3"/><circle cx="112" cy="63" r="1.3"/><circle cx="150" cy="63" r="1.3"/><circle cx="189" cy="63" r="1.3"/></g>
    <g stroke="#c9ccd2" stroke-width=".4"><line x1="73" y1="45" x2="73" y2="62"/><line x1="150" y1="45" x2="150" y2="62"/><line x1="35" y1="64" x2="35" y2="70"/><line x1="112" y1="64" x2="112" y2="70"/><line x1="189" y1="64" x2="189" y2="70"/></g>
  </svg>
  <div class="abs" style="left:53px;top:28px;width:40px;text-align:center"><div class="h" style="color:var(--ink)">2012</div><div class="p">A key milestone for the firm.</div></div>
  <div class="abs" style="left:130px;top:28px;width:40px;text-align:center"><div class="h" style="color:var(--ink)">2014</div><div class="p">A key milestone for the firm.</div></div>
  <div class="abs" style="left:15px;top:71px;width:40px;text-align:center"><div class="h" style="color:var(--ink)">2011</div><div class="p">A key milestone for the firm.</div></div>
  <div class="abs" style="left:92px;top:71px;width:40px;text-align:center"><div class="h" style="color:var(--ink)">2013</div><div class="p">A key milestone for the firm.</div></div>
  <div class="abs" style="left:169px;top:71px;width:40px;text-align:center"><div class="h" style="color:var(--ink)">2015</div><div class="p">A key milestone for the firm.</div></div>
  <div class="foot-brand"><span class="mark"></span>Northbay<br>Financial</div><svg class="foot-chev"><use href="#chev"/></svg>
</section>

<!-- 18 Image left -->
<section class="slide">
  <div class="title"><b>Image slide</b></div>
  <div class="photo dark" role="img" aria-label="Trading screen with market charts" style="left:11px;top:31px;width:95px;height:56px"></div>
  <div class="abs" style="left:115px;top:31px;width:95px"><div class="h" style="color:var(--ink)">Opening point here</div><div class="p">A short paragraph to sit beside the image and set out the main idea.</div>
    <ul class="b p" style="margin-top:3px"><li>First supporting point here.</li><li>Second supporting point here.</li><li>Third supporting point here.</li></ul></div>
  <div class="foot-brand"><span class="mark"></span>Northbay<br>Financial</div><svg class="foot-chev"><use href="#chev"/></svg>
</section>

<!-- 19 Image right -->
<section class="slide">
  <div class="title"><b>Image slide</b></div>
  <div class="abs" style="left:11px;top:31px;width:95px"><div class="h" style="color:var(--ink)">Opening point here</div><div class="p">A short paragraph to sit beside the image and set out the main idea.</div>
    <ul class="b p" style="margin-top:3px"><li>First supporting point here.</li><li>Second supporting point here.</li><li>Third supporting point here.</li></ul></div>
  <div class="photo dark" role="img" aria-label="Trading screen with market charts" style="left:115px;top:31px;width:95px;height:56px"></div>
  <div class="foot-brand"><span class="mark"></span>Northbay<br>Financial</div><svg class="foot-chev"><use href="#chev"/></svg>
</section>

<!-- 20 Two images -->
<section class="slide">
  <div class="title"><b>Image slide</b></div>
  <div class="photo light" role="img" aria-label="Bright modern office desk" style="left:15px;top:33px;width:92px;height:46px"></div>
  <div class="photo dark" role="img" aria-label="Trading screen with market charts" style="left:114px;top:33px;width:92px;height:46px"></div>
  <div class="abs navy" style="left:15px;top:77px;width:92px;height:5px;font-size:2.4px;color:#fff;text-align:center;line-height:5px;font-weight:700">HEADING TEXT</div>
  <div class="abs navy" style="left:114px;top:77px;width:92px;height:5px;font-size:2.4px;color:#fff;text-align:center;line-height:5px;font-weight:700">HEADING TEXT</div>
  <div class="abs p" style="left:15px;top:85px;width:92px">A short caption about this picture and its point.</div>
  <div class="abs p" style="left:114px;top:85px;width:92px">A short caption about this picture and its point.</div>
  <div class="foot-brand"><span class="mark"></span>Northbay<br>Financial</div><svg class="foot-chev"><use href="#chev"/></svg>
</section>

<!-- 21 Three images -->
<section class="slide">
  <div class="title"><b>Image slide</b></div>
  <div class="photo" role="img" aria-label="Colleagues meeting around a laptop" style="left:11px;top:26px;width:63px;height:40px"></div>
  <div class="photo light" role="img" aria-label="Printed financial charts on a desk" style="left:79px;top:26px;width:63px;height:40px"></div>
  <div class="photo" role="img" aria-label="Hands holding a tablet" style="left:147px;top:26px;width:63px;height:40px"></div>
  <div class="abs" style="left:11px;top:70px;width:63px"><div class="h">Heading text</div><div class="p">A short caption about this picture and its point.</div></div>
  <div class="abs" style="left:79px;top:70px;width:63px"><div class="h">Heading text</div><div class="p">A short caption about this picture and its point.</div></div>
  <div class="abs" style="left:147px;top:70px;width:63px"><div class="h">Heading text</div><div class="p">A short caption about this picture and its point.</div></div>
  <div class="foot-brand"><span class="mark"></span>Northbay<br>Financial</div><svg class="foot-chev"><use href="#chev"/></svg>
</section>

<!-- 22 Collage + list -->
<section class="slide">
  <div class="title"><b>Image slide</b></div>
  <div class="photo" role="img" aria-label="Business team gathered in discussion" style="left:11px;top:26px;width:86px;height:61px"></div>
  <div class="photo light" role="img" aria-label="Printed financial charts" style="left:100px;top:26px;width:40px;height:29px"></div>
  <div class="photo" role="img" aria-label="Hand holding a tablet" style="left:100px;top:58px;width:40px;height:29px"></div>
  <div class="abs" style="left:11px;top:90px;width:80px"><div class="h">• Heading text</div><div class="p">A short caption about this image.</div></div>
  <div class="abs" style="left:146px;top:27px;width:64px;display:grid;row-gap:4px">
    <div><div class="h">• Heading text</div><div class="p">A brief line about this point.</div></div>
    <div><div class="h">• Heading text</div><div class="p">A brief line about this point.</div></div>
    <div><div class="h">• Heading text</div><div class="p">A brief line about this point.</div></div>
  </div>
  <div class="foot-brand"><span class="mark"></span>Northbay<br>Financial</div><svg class="foot-chev"><use href="#chev"/></svg>
</section>

<!-- 23 Portfolio -->
<section class="slide">
  <div class="title"><b>Our portfolio</b></div>
  <div class="photo dark" role="img" aria-label="Trading screen with market charts" style="left:11px;top:26px;width:68px;height:88px"></div>
  <div class="photo light" role="img" aria-label="Office with large windows" style="left:81px;top:26px;width:64px;height:43px"></div>
  <div class="photo" role="img" aria-label="Person typing on a laptop" style="left:147px;top:26px;width:64px;height:43px"></div>
  <div class="photo" role="img" aria-label="Tablet showing charts" style="left:81px;top:71px;width:40px;height:43px"></div>
  <div class="photo light" role="img" aria-label="Meeting room" style="left:123px;top:71px;width:40px;height:43px"></div>
  <div class="photo light" role="img" aria-label="Printed reports on a desk" style="left:165px;top:71px;width:46px;height:43px"></div>
</section>

<!-- 24 Portfolio grid -->
<section class="slide">
  <div class="title"><b>Our portfolio</b></div>
  <div class="photo" role="img" aria-label="Business team meeting" style="left:11px;top:26px;width:50px;height:43px"></div>
  <div class="photo" role="img" aria-label="Colleagues at a desk" style="left:11px;top:71px;width:50px;height:43px"></div>
  <div class="photo" role="img" aria-label="Reviewing documents together" style="left:63px;top:26px;width:43px;height:43px"></div>
  <div class="photo light" role="img" aria-label="Financial charts" style="left:63px;top:71px;width:43px;height:43px"></div>
  <div class="photo" role="img" aria-label="Laptop and notes" style="left:108px;top:26px;width:49px;height:28px"></div>
  <div class="photo light" role="img" aria-label="Bright office interior" style="left:108px;top:56px;width:49px;height:28px"></div>
  <div class="photo light" role="img" aria-label="Charts on a desk" style="left:108px;top:86px;width:49px;height:28px"></div>
  <div class="photo light" role="img" aria-label="Printed reports" style="left:159px;top:26px;width:52px;height:28px"></div>
  <div class="photo" role="img" aria-label="Tablet in hand" style="left:159px;top:56px;width:52px;height:28px"></div>
  <div class="photo dark" role="img" aria-label="Market screen" style="left:159px;top:86px;width:52px;height:28px"></div>
</section>

<!-- 25 Image mosaic -->
<section class="slide">
  <div class="title"><b>Image slide</b></div>
  <div class="photo light" role="img" aria-label="Meeting room" style="left:0;top:26px;width:37px;height:34px"></div>
  <div class="abs navy pw" style="left:37px;top:26px;width:37px;height:34px;padding:4px">A short note on this point.</div>
  <div class="photo dark" role="img" aria-label="Conference room" style="left:74px;top:26px;width:37px;height:34px"></div>
  <div class="abs navy pw" style="left:111px;top:26px;width:37px;height:34px;padding:4px">A short note on this point.</div>
  <div class="photo light" role="img" aria-label="Charts on paper" style="left:148px;top:26px;width:37px;height:34px"></div>
  <div class="abs pw" style="left:185px;top:26px;width:37px;height:34px;padding:4px;background:var(--charcoal)">A short note on this point.</div>
  <div class="abs navy pw" style="left:0;top:60px;width:37px;height:34px;padding:4px">A short note on this point.</div>
  <div class="photo" role="img" aria-label="Board room table" style="left:37px;top:60px;width:37px;height:34px"></div>
  <div class="abs pw" style="left:74px;top:60px;width:37px;height:34px;padding:4px;background:var(--charcoal)">A short note on this point.</div>
  <div class="photo light" role="img" aria-label="Office desk" style="left:111px;top:60px;width:37px;height:34px"></div>
  <div class="abs navy pw" style="left:148px;top:60px;width:37px;height:34px;padding:4px">A short note on this point.</div>
  <div class="photo light" role="img" aria-label="Printed reports" style="left:185px;top:60px;width:37px;height:34px"></div>
  <div class="foot-brand"><span class="mark"></span>Northbay<br>Financial</div><svg class="foot-chev"><use href="#chev"/></svg>
</section>

<!-- 26 Dark divider -->
<section class="slide" style="background:linear-gradient(135deg,#4a4a4a,#2e2e2e)">
  <svg class="abs" style="left:28px;top:55px" width="17" height="17" viewBox="0 0 10 10"><path d="M2 8h6M2.8 7.6V5M4.3 7.6V3.6M5.8 7.6V4.3M7.3 7.6V2.6" stroke="#fff" stroke-width=".6" fill="none"/></svg>
  <div class="abs" style="left:28px;top:80px;font-size:4.4px;color:#fff">SECTION DIVIDER</div>
  <div class="abs" style="left:28px;top:87px;width:110px;font-size:2.4px;line-height:3.4px;color:#b8b8b8">A short line that introduces the section ahead.</div>
</section>

<!-- 27 Donuts -->
<section class="slide">
  <div class="title"><b>Chart and diagram</b> slide</div>
  <svg class="abs" style="left:0;top:0" width="221.6" height="124">
    <g fill="none" stroke-width="3">
      <circle cx="46" cy="60" r="13" stroke="#d5d8de"/><circle cx="46" cy="60" r="13" stroke="#1f3a6e" stroke-dasharray="49 82" transform="rotate(-90 46 60)"/>
      <circle cx="111" cy="60" r="13" stroke="#d5d8de"/><circle cx="111" cy="60" r="13" stroke="#1f3a6e" stroke-dasharray="32.7 82" transform="rotate(-90 111 60)"/>
      <circle cx="176" cy="60" r="13" stroke="#d5d8de"/><circle cx="176" cy="60" r="13" stroke="#1f3a6e" stroke-dasharray="20.4 82" transform="rotate(-90 176 60)"/>
    </g>
    <g font-family="Montserrat,sans-serif" font-size="4.2" font-weight="700" fill="#1f3a6e" text-anchor="middle"><text x="46" y="61.5">60%</text><text x="111" y="61.5">40%</text><text x="176" y="61.5">25%</text></g>
  </svg>
  <div class="abs" style="left:21px;top:79px;width:50px;text-align:center"><div class="h">Heading text</div><div class="p">A short line about this figure.</div></div>
  <div class="abs" style="left:86px;top:79px;width:50px;text-align:center"><div class="h">Heading text</div><div class="p">A short line about this figure.</div></div>
  <div class="abs" style="left:151px;top:79px;width:50px;text-align:center"><div class="h">Heading text</div><div class="p">A short line about this figure.</div></div>
  <div class="foot-brand"><span class="mark"></span>Northbay<br>Financial</div><svg class="foot-chev"><use href="#chev"/></svg>
</section>

<!-- 28 Bar groups -->
<section class="slide">
  <div class="title"><b>Chart and diagram</b> slide</div>
  <div class="abs p" style="left:11px;top:19px;width:199px;text-align:center">A short intro line that explains what the chart below shows.</div>
  <svg class="abs" style="left:0;top:0" width="221.6" height="124">
    <g font-family="Montserrat,sans-serif" font-size="2" fill="#8c8c8c"><rect x="80" y="29" width="3" height="2" fill="#1f3a6e"/><text x="84" y="31">Series one</text><rect x="101" y="29" width="3" height="2" fill="#3b3b3b"/><text x="105" y="31">Series two</text><rect x="122" y="29" width="3" height="2" fill="#b5b5b5"/><text x="126" y="31">Series three</text></g>
    <g>
      <rect x="30" y="73" width="5" height="14" fill="#1f3a6e"/><rect x="36" y="68" width="5" height="19" fill="#3b3b3b"/><rect x="42" y="62" width="5" height="25" fill="#b5b5b5"/>
      <rect x="77" y="70" width="5" height="17" fill="#1f3a6e"/><rect x="83" y="76" width="5" height="11" fill="#3b3b3b"/><rect x="89" y="67" width="5" height="20" fill="#b5b5b5"/>
      <rect x="125" y="68" width="5" height="19" fill="#1f3a6e"/><rect x="131" y="62" width="5" height="25" fill="#3b3b3b"/><rect x="137" y="73" width="5" height="14" fill="#b5b5b5"/>
      <rect x="172" y="72" width="5" height="15" fill="#1f3a6e"/><rect x="178" y="77" width="5" height="10" fill="#3b3b3b"/><rect x="184" y="66" width="5" height="21" fill="#b5b5b5"/>
    </g>
    <g font-family="Montserrat,sans-serif" font-size="2.4" font-weight="700" fill="#1f3a6e" text-anchor="middle"><text x="38.5" y="92">HEADING TEXT</text><text x="85.5" y="92">HEADING TEXT</text><text x="133.5" y="92">HEADING TEXT</text><text x="180.5" y="92">HEADING TEXT</text></g>
  </svg>
  <div class="foot-brand"><span class="mark"></span>Northbay<br>Financial</div><svg class="foot-chev"><use href="#chev"/></svg>
</section>

<!-- 29 Bar chart -->
<section class="slide">
  <div class="title"><b>Chart and diagram</b> slide</div>
  <svg class="abs" style="left:0;top:0" width="221.6" height="124">
    <g stroke="#e1e3e7" stroke-width=".3"><line x1="20" y1="38" x2="140" y2="38"/><line x1="20" y1="50" x2="140" y2="50"/><line x1="20" y1="62" x2="140" y2="62"/><line x1="20" y1="74" x2="140" y2="74"/></g>
    <line x1="20" y1="86" x2="140" y2="86" stroke="#b5b5b5" stroke-width=".4"/>
    <g font-family="Montserrat,sans-serif" font-size="2" fill="#8c8c8c"><text x="14" y="39">40</text><text x="14" y="51">30</text><text x="14" y="63">20</text><text x="14" y="75">10</text><text x="16" y="87">0</text>
      <text x="31" y="91">2012</text><text x="57" y="91">2014</text><text x="88" y="91">2016</text><text x="117" y="91">2018</text></g>
    <rect x="32" y="69" width="4" height="17" fill="#1f3a6e"/><rect x="40" y="61" width="4" height="25" fill="#b5b5b5"/>
    <rect x="59" y="42" width="4" height="44" fill="#1f3a6e"/><rect x="67" y="50" width="4" height="36" fill="#b5b5b5"/>
    <rect x="89" y="58" width="4" height="28" fill="#1f3a6e"/><rect x="97" y="66" width="4" height="20" fill="#b5b5b5"/>
    <rect x="118" y="65" width="4" height="21" fill="#1f3a6e"/><rect x="126" y="48" width="4" height="38" fill="#b5b5b5"/>
    <g font-family="Montserrat,sans-serif" font-size="2" fill="#8c8c8c"><rect x="55" y="95" width="3" height="2" fill="#1f3a6e"/><text x="59" y="97">Series one</text><rect x="80" y="95" width="3" height="2" fill="#b5b5b5"/><text x="84" y="97">Series two</text></g>
  </svg>
  <div class="abs" style="left:152px;top:32px;width:58px;display:grid;row-gap:4px">
    <div><div class="h">• Heading text</div><div class="p">A brief line about this data.</div></div>
    <div><div class="h">• Heading text</div><div class="p">A brief line about this data.</div></div>
    <div><div class="h">• Heading text</div><div class="p">A brief line about this data.</div></div>
    <div><div class="h">• Heading text</div><div class="p">A brief line about this data.</div></div>
  </div>
  <div class="foot-brand"><span class="mark"></span>Northbay<br>Financial</div><svg class="foot-chev"><use href="#chev"/></svg>
</section>

<!-- 30 Table -->
<section class="slide">
  <div class="title"><b>Chart and diagram</b> slide</div>
  <svg class="abs" style="left:0;top:0" width="221.6" height="124">
    <g fill="#1f3a6e"><rect x="15" y="40" width="38" height="5"/><rect x="91" y="40" width="38" height="5"/><rect x="167" y="40" width="38" height="5"/></g>
    <g fill="#3b3b3b"><rect x="53" y="40" width="38" height="5"/><rect x="129" y="40" width="38" height="5"/></g>
    <g fill="#f0f1f4"><rect x="15" y="51" width="190" height="5"/><rect x="15" y="61" width="190" height="5"/><rect x="15" y="71" width="190" height="5"/><rect x="15" y="81" width="190" height="5"/></g>
    <g font-family="Montserrat,sans-serif" font-size="2" fill="#fff" font-weight="600"><text x="19" y="43.3">Label one</text><text x="57" y="43.3">Label two</text><text x="95" y="43.3">Label three</text><text x="133" y="43.3">Label four</text><text x="171" y="43.3">Label five</text></g>
    <g font-family="Montserrat,sans-serif" font-size="2" fill="#8c8c8c">
      <text x="19" y="49">Item</text><text x="57" y="49">Value</text><text x="95" y="49">Value</text><text x="133" y="49">Value</text><text x="171" y="49">Value</text>
      <text x="19" y="54">Item</text><text x="57" y="54">Value</text><text x="95" y="54">Value</text><text x="133" y="54">Value</text><text x="171" y="54">Value</text>
      <text x="19" y="59">Item</text><text x="57" y="59">Value</text><text x="95" y="59">Value</text><text x="133" y="59">Value</text><text x="171" y="59">Value</text>
      <text x="19" y="64">Item</text><text x="57" y="64">Value</text><text x="95" y="64">Value</text><text x="133" y="64">Value</text><text x="171" y="64">Value</text>
      <text x="19" y="69">Item</text><text x="57" y="69">Value</text><text x="95" y="69">Value</text><text x="133" y="69">Value</text><text x="171" y="69">Value</text>
      <text x="19" y="74">Item</text><text x="57" y="74">Value</text><text x="95" y="74">Value</text><text x="133" y="74">Value</text><text x="171" y="74">Value</text>
      <text x="19" y="79">Item</text><text x="57" y="79">Value</text><text x="95" y="79">Value</text><text x="133" y="79">Value</text><text x="171" y="79">Value</text>
      <text x="19" y="84">Item</text><text x="57" y="84">Value</text><text x="95" y="84">Value</text><text x="133" y="84">Value</text><text x="171" y="84">Value</text>
    </g>
  </svg>
  <div class="abs p" style="left:15px;top:90px;width:190px;text-align:center">A short note that explains the figures set out in the table above.</div>
  <div class="foot-brand"><span class="mark"></span>Northbay<br>Financial</div><svg class="foot-chev"><use href="#chev"/></svg>
</section>

<!-- 31 Process curve -->
<section class="slide">
  <div class="title"><b>Proccess</b> slide</div>
  <svg class="abs" style="left:0;top:0" width="221.6" height="124">
    <path d="M28 82 Q50 76 60 84 Q78 96 100 82 L155 48" fill="none" stroke="#b5b5b5" stroke-width=".5"/>
    <path d="M155 48 L162 41" stroke="#b5b5b5" stroke-width=".5"/><path d="M160 40l3-.5-.5 3" fill="none" stroke="#b5b5b5" stroke-width=".5"/>
    <g fill="#fff" stroke="#1f3a6e" stroke-width=".6"><circle cx="60" cy="84" r="4"/><circle cx="100" cy="82" r="4"/><circle cx="118" cy="71" r="4"/><circle cx="137" cy="59" r="4"/><circle cx="155" cy="48" r="4"/></g>
    <g fill="#1f3a6e"><circle cx="60" cy="84" r="1.3"/><circle cx="100" cy="82" r="1.3"/><circle cx="118" cy="71" r="1.3"/><circle cx="137" cy="59" r="1.3"/><circle cx="155" cy="48" r="1.3"/></g>
  </svg>
  <div class="abs" style="left:28px;top:62px;width:40px"><div class="h" style="color:var(--ink)">Step 1</div><div class="p">A brief line about this step.</div></div>
  <div class="abs" style="left:92px;top:92px;width:40px"><div class="h" style="color:var(--ink)">Step 2</div><div class="p">A brief line about this step.</div></div>
  <div class="abs" style="left:78px;top:50px;width:40px"><div class="h" style="color:var(--ink)">Step 3</div><div class="p">A brief line about this step.</div></div>
  <div class="abs" style="left:150px;top:68px;width:40px"><div class="h" style="color:var(--ink)">Step 4</div><div class="p">A brief line about this step.</div></div>
  <div class="abs" style="left:108px;top:26px;width:40px"><div class="h" style="color:var(--ink)">Step 5</div><div class="p">A brief line about this step.</div></div>
  <div class="foot-brand"><span class="mark"></span>Northbay<br>Financial</div><svg class="foot-chev"><use href="#chev"/></svg>
</section>

<!-- 32 Process diamonds -->
<section class="slide">
  <div class="title"><b>Proccess</b> slide</div>
  <svg class="abs" style="left:0;top:0" width="221.6" height="124">
    <polygon points="16,46 30,34 44,46 30,58" fill="#1f3a6e"/>
    <polygon points="51,46 65,34 79,46 65,58" fill="#9a9a9a"/>
    <polygon points="86,46 100,34 114,46 100,58" fill="#3b3b3b"/>
    <polygon points="121,46 135,34 149,46 135,58" fill="#9a9a9a"/>
    <polygon points="156,46 170,34 184,46 170,58" fill="#1f3a6e"/>
    <use href="#target" x="26" y="42" width="8" height="8"/><use href="#chart" x="61" y="42" width="8" height="8"/><use href="#target" x="96" y="42" width="8" height="8"/><use href="#case" x="131" y="42" width="8" height="8"/><use href="#doc" x="166" y="42" width="8" height="8"/>
  </svg>
  <div class="abs" style="left:16px;top:63px;width:30px"><div class="h" style="color:var(--ink)">Step 1</div><div class="p">A brief line about this step.</div></div>
  <div class="abs" style="left:51px;top:63px;width:30px"><div class="h" style="color:var(--ink)">Step 2</div><div class="p">A brief line about this step.</div></div>
  <div class="abs" style="left:86px;top:63px;width:30px"><div class="h" style="color:var(--ink)">Step 3</div><div class="p">A brief line about this step.</div></div>
  <div class="abs" style="left:121px;top:63px;width:30px"><div class="h" style="color:var(--ink)">Step 4</div><div class="p">A brief line about this step.</div></div>
  <div class="abs" style="left:156px;top:63px;width:30px"><div class="h" style="color:var(--ink)">Step 5</div><div class="p">A brief line about this step.</div></div>
  <div class="foot-brand"><span class="mark"></span>Northbay<br>Financial</div><svg class="foot-chev"><use href="#chev"/></svg>
</section>

<!-- 33 Process cycle -->
<section class="slide">
  <div class="title"><b>Proccess</b> slide</div>
  <svg class="abs" style="left:0;top:0" width="221.6" height="124" viewBox="0 0 221.6 124">
    <g fill="none" stroke-width="10">
      <path d="M113 43 A22 22 0 0 1 131 61" stroke="#9a9a9a"/>
      <path d="M131 67 A22 22 0 0 1 113 85" stroke="#1f3a6e"/>
      <path d="M107 85 A22 22 0 0 1 89 67" stroke="#9a9a9a"/>
      <path d="M89 61 A22 22 0 0 1 107 43" stroke="#1f3a6e"/>
    </g>
    <circle cx="110" cy="64" r="9" fill="#1f3a6e"/><rect x="107" y="61" width="6" height="6" fill="#fff"/>
    <use href="#chart" x="117" y="46" width="8" height="8"/><use href="#case" x="117" y="74" width="8" height="8"/><use href="#target" x="95" y="74" width="8" height="8"/><use href="#doc" x="95" y="46" width="8" height="8"/>
  </svg>
  <div class="abs" style="left:40px;top:44px;width:40px;text-align:right"><div class="h" style="color:var(--ink)">Step 1</div><div class="p">A brief line about this step.</div></div>
  <div class="abs" style="left:142px;top:38px;width:40px"><div class="h" style="color:var(--ink)">Step 2</div><div class="p">A brief line about this step.</div></div>
  <div class="abs" style="left:150px;top:62px;width:40px"><div class="h" style="color:var(--ink)">Step 3</div><div class="p">A brief line about this step.</div></div>
  <div class="abs" style="left:142px;top:86px;width:40px"><div class="h" style="color:var(--ink)">Step 4</div><div class="p">A brief line about this step.</div></div>
  <div class="abs" style="left:40px;top:80px;width:40px;text-align:right"><div class="h" style="color:var(--ink)">Step 5</div><div class="p">A brief line about this step.</div></div>
  <div class="foot-brand"><span class="mark"></span>Northbay<br>Financial</div><svg class="foot-chev"><use href="#chev"/></svg>
</section>

<!-- 34 Hierarchy -->
<section class="slide">
  <div class="title"><b>Hierarchy</b> slide</div>
  <svg class="abs" style="left:0;top:0" width="221.6" height="124">
    <polygon points="110,30 117,43 103,43" fill="#1f3a6e"/>
    <polygon points="102,45 118,45 125,58 95,58" fill="#9a9a9a"/>
    <polygon points="94,60 126,60 133,73 87,73" fill="#3b3b3b"/>
    <polygon points="86,75 134,75 141,88 79,88" fill="#9a9a9a"/>
    <polygon points="78,90 142,90 149,103 71,103" fill="#1f3a6e"/>
  </svg>
  <div class="abs" style="left:150px;top:29px;width:44px"><div class="h" style="color:var(--ink)">Heading 1</div><div class="p">A brief line for this level.</div></div>
  <div class="abs" style="left:40px;top:44px;width:44px;text-align:right"><div class="h" style="color:var(--ink)">Heading 2</div><div class="p">A brief line for this level.</div></div>
  <div class="abs" style="left:150px;top:59px;width:44px"><div class="h" style="color:var(--ink)">Heading 3</div><div class="p">A brief line for this level.</div></div>
  <div class="abs" style="left:36px;top:74px;width:44px;text-align:right"><div class="h" style="color:var(--ink)">Heading 4</div><div class="p">A brief line for this level.</div></div>
  <div class="abs" style="left:150px;top:89px;width:44px"><div class="h" style="color:var(--ink)">Heading 5</div><div class="p">A brief line for this level.</div></div>
  <div class="foot-brand"><span class="mark"></span>Northbay<br>Financial</div><svg class="foot-chev"><use href="#chev"/></svg>
</section>

<!-- 35 Coffee break -->
<section class="slide">
  <div class="photo" role="img" aria-label="Black and white cup of coffee on a table" style="inset:0;background:linear-gradient(135deg,#9c9c9c,#3f3f3f)"></div>
  <div class="abs" style="left:-6px;top:14px;width:100px;height:100px;border-radius:50%;background:var(--navy);opacity:.9"></div>
  <div class="abs" style="left:33px;top:46px;font-size:13px;color:#fff;font-weight:300;line-height:13px">01.</div>
  <div class="abs" style="left:33px;top:61px;font-size:4.2px;color:#fff">COFFEE BREAK</div>
  <div class="abs pw" style="left:33px;top:67px">We'll be back in 15 minutes</div>
</section>

<!-- 36 Thank you -->
<section class="slide">
  <div class="abs" style="left:0;top:0;width:100%;height:84px;background:linear-gradient(135deg,#2a4679,#172d57)" role="img" aria-label="City buildings in navy tone"></div>
  <div class="abs" style="left:0;right:0;top:53px;text-align:center;font-size:4.4px;color:#fff">THANK YOU FOR WATCHING</div>
  <div class="abs pw" style="left:0;right:0;top:60px;text-align:center">Questions are always welcome.</div>
  <div class="brand-big abs" style="left:17px;top:95px;font-size:3px;line-height:3.4px"><span class="mark" style="width:8px;height:8px"></span>Northbay<br>Financial Group</div>
  <div class="abs" style="left:98px;top:93px;width:30px"><div class="h" style="color:var(--ink);font-size:2.2px">Address</div><div class="p" style="font-size:2px;line-height:2.8px">20 Harbor Lane<br>Suite 400</div></div>
  <div class="abs" style="left:146px;top:93px;width:25px"><div class="h" style="color:var(--ink);font-size:2.2px">Contact</div><div class="p" style="font-size:2px;line-height:2.8px">+1 555 0148<br>+1 555 0172</div></div>
  <div class="abs" style="left:175px;top:93px;width:40px"><div class="h" style="color:var(--ink);font-size:2.2px">Email &amp; Website</div><div class="p" style="font-size:2px;line-height:2.8px">hello@northbayfinancial.com<br>northbayfinancial.com</div></div>
</section>

</main>
</body>
</html>
```